Southport Billboard for Hiring more CDL drivers

I need a catch design for a bill board (size 10ft by 36 ft) to catch the attention for semi truck drivers.
In the design I want it to include:
-My company logo along with my website(brisklanefreighters.com) and my number(503-217-6095) for contact info.
-I also need it to say earn up to $90,000 a year
-I will send a few photos to choose from
-I need the logo to look clean and simple! I don't want it to be cluttered just clean, simple and catchy.!

Target Market(s)

CDL Class A holders
Semi Truck Drivers

Industry/Entity Type

Trucking Company

Font styles to use
Other font styles liked:
• a font to match my logo

Requirements
Must have
• "Make up to $90,000"
"brisklanefreighters.com"
"503-217-6095"

```html
<!DOCTYPE html>
<html lang="en">
<head>
<meta charset="UTF-8">
<title>Brisk Lane Freighters – Driver Hiring Billboard</title>
<link href="https://fonts.googleapis.com/css2?family=Anton&family=Oswald:wght@600;700&family=Roboto+Condensed:wght@500;700&display=swap" rel="stylesheet">
<style>
  :root {
    --page: #e9ecef;
    --board: #ffffff;
    --ink: #1f231f;
    --red: #e21b22;
    --bar: #0d0d0d;
    --bar-text: #ffffff;
    --photo-sky: #c9d2da;
    --photo-mid: #8e9a8f;
    --photo-ground: #b7b0a2;
  }
  * { box-sizing: border-box; margin: 0; padding: 0; }
  html, body { width: 1200px; height: 800px; overflow: hidden; background: var(--page); }
  .billboard {
    position: absolute; left: 20px; top: 239px;
    width: 1160px; height: 322px;
    background: var(--board);
    box-shadow: 0 4px 18px rgba(0,0,0,.15);
  }
  .brand {
    position: absolute; left: 40px; top: 34px; width: 280px;
    font-family: "Anton", sans-serif; color: var(--ink);
    font-size: 62px; line-height: 1.02; letter-spacing: 1px;
    text-transform: uppercase;
  }
  .photo {
    position: absolute; left: 336px; top: 6px; width: 450px; height: 252px;
    background: radial-gradient(ellipse at 55% 55%, var(--photo-mid) 0%, var(--photo-sky) 55%, rgba(255,255,255,0) 78%),
                linear-gradient(180deg, rgba(255,255,255,0) 60%, var(--photo-ground) 85%, rgba(255,255,255,0) 100%);
  }
  .offer {
    position: absolute; left: 800px; top: 24px; width: 330px; height: 200px;
    text-align: center; font-family: "Oswald", sans-serif; font-weight: 700;
    color: var(--ink); text-transform: uppercase;
  }
  .offer-frame { position: absolute; inset: 0; }
  .offer-lead { position: absolute; top: 2px; left: 0; right: 0; font-size: 44px; line-height: 1; letter-spacing: 1px; }
  .offer-amount { position: absolute; top: 54px; left: 0; right: 0; font-size: 88px; line-height: 1; color: var(--red); }
  .offer-tail { position: absolute; top: 156px; left: 0; right: 0; font-size: 44px; line-height: 1; letter-spacing: 1px; }
  .contact-bar {
    position: absolute; left: 156px; top: 261px; width: 844px; height: 61px;
    background: var(--bar); border-radius: 14px 14px 0 0;
    display: flex; align-items: center; justify-content: center; gap: 54px;
    color: var(--bar-text);
  }
  .contact-item { display: flex; align-items: center; gap: 12px; }
  .contact-icon { width: 36px; height: 36px; }
  .contact-phone { font-family: "Roboto Condensed", sans-serif; font-weight: 700; font-size: 40px; letter-spacing: .5px; }
  .contact-web { font-family: "Roboto Condensed", sans-serif; font-weight: 500; font-size: 32px; }
</style>
</head>
<body>
  <div class="billboard">
    <div class="brand">Brisk Lane<br>Freighters</div>

    <div class="photo" role="img" aria-label="Photo of a green semi truck hauling white cargo vans on a car-carrier trailer under a cloudy sky"></div>

    <div class="offer">
      <svg class="offer-frame" viewBox="0 0 330 200" fill="none" stroke="#1f231f" stroke-width="3">
        <path d="M22 20 H4 V140"/>
        <path d="M326 60 V182 H290"/>
        <path d="M40 176 H4"/>
        <path d="M290 20 H326"/>
      </svg>
      <div class="offer-lead">Earn up to</div>
      <div class="offer-amount">$90,000</div>
      <div class="offer-tail">A year</div>
    </div>

    <div class="contact-bar">
      <div class="contact-item">
        <svg class="contact-icon" viewBox="0 0 36 36" fill="none" stroke="#fff" stroke-width="2.4">
          <circle cx="18" cy="18" r="16"/>
          <path d="M13 10 l3 4 -2 2 c1 3 3 5 6 6 l2 -2 4 3 -2 3 c-7 0 -14 -7 -14 -14 z" fill="#fff" stroke-width="1"/>
        </svg>
        <span class="contact-phone">503-217-6095</span>
      </div>
      <div class="contact-item">
        <svg class="contact-icon" viewBox="0 0 36 36" fill="none" stroke="#fff" stroke-width="2">
          <circle cx="18" cy="18" r="16"/>
          <circle cx="18" cy="18" r="10"/>
          <ellipse cx="18" cy="18" rx="4.5" ry="10"/>
          <path d="M8 18 H28 M10 13 H26 M10 23 H26"/>
        </svg>
        <span class="contact-web">brisklanefreighters.com</span>
      </div>
    </div>
  </div>
</body>
</html>
```